Young company in the agrifood product sector *

Our company% 26 # 233; t% 26 # 233; Amber Ridge low% 26 # 233; % 26 # 224; Toulouse et sp% 26 # 233; cialis% 26 # 233; in the packaging and marketing of beehive products, We need a design of% 26 # 39;% 26 # 39;% 26 # 233; label for honey jar of 250g, The% 26 # 233; labels destiny% 26 # 233; the honey jars will be transparent so that the nectar is visible from the front, our Amber Ridge logo must be% 26 # 234; be located% 26 # 233; above / middle of% 26 # 393% label followed below the appellation, for example Ch% 26 # 226; taignier followed below the country of% 26 # 39; origin France tracking below r% 26 # 233; region of r% 26 # 233; colte Midi-Pyr% 26 # 233; n% 26 # 233; es and below l% 26 # 39;% 26 # 233; label weight 250g and% 26lt;% 26lt;% 26lt; Honey% 26gt;% 26gt; on the% 26 # 39;% 26 # 233; label will be a plus but optional, The dimensions of the% 26 # 39;% 26 # 233; label are the following 6cm x 6cm. The design must inspire quality% 26 # 233; luxury, l% 26 # 39;% 26 # 233; l% 26 # 233; elegance and confidence, these are quality honey% 26 # 233; and rare honeys from around the world which are very expensive. Very important, the honeys have different colors, this can range from white to orange yellow or darker shades of brown% 26 # 234; black, that's why we would like to have at least 3 colors for light honey, medium dark% 26 # 233; and dark% 26 # 233 ;, Regarding the colors you have free choice of course% 26 # 251; r taking into account the colors of the honey which must% 26 # 234; be visible% 26 # 224; through the% 26 # 39;% 26 # 233; transparent label You will find attached the files of our Ambre Ridge logo. 20%% 26 # 224; 40% transparency on the% 26 # 39;% 26 # 233; label would be reasonable but% 26 # 224; you to see which is better, thanks
- Krone one

```html
<!DOCTYPE html>
<html lang="fr">
<head>
<meta charset="utf-8">
<title>Ambre Ridge – Châtaignier 250g labels</title>
<link rel="stylesheet" href="https://fonts.googleapis.com/css2?family=Varela+Round&family=Tinos&display=swap">
<style>
  :root {
    --page: #ffffff;
    --honey-light: #f9ad2a;
    --honey-deep: #ee8318;
    --ink-dark: #15172a;
    --label-white: #ffffff;
    --amber: #f0961e;
    --amber-text: #f39a1c;
  }
  * { margin: 0; padding: 0; box-sizing: border-box; }
  html, body {
    width: 1200px;
    height: 1200px;
    overflow: hidden;
    background: var(--page);
  }
  .label-sheet {
    width: 1200px;
    height: 1200px;
    display: flex;
    align-items: center;
    justify-content: center;
    gap: 80px;
  }
  .label {
    width: 500px;
    height: 640px;
    display: block;
  }
  .honey-field { fill: url(#honey); }
  .label--dark .label-shape { fill: var(--ink-dark); }
  .label--light .label-shape { fill: var(--label-white); }
  .brand-name {
    font-family: "Varela Round", sans-serif;
    font-size: 34px;
    fill: var(--amber);
  }
  .brand-name--tag { font-size: 26px; }
  .brand-dot { fill: var(--amber); }
  .appellation {
    font-family: "Varela Round", sans-serif;
    font-size: 40px;
    letter-spacing: 2px;
    fill: var(--amber-text);
  }
  .origin-country {
    font-family: "Tinos", serif;
    font-size: 27px;
    fill: var(--amber-text);
  }
  .origin-region {
    font-family: "Tinos", serif;
    font-size: 20px;
    fill: var(--amber-text);
    letter-spacing: -0.5px;
  }
  .net-weight {
    font-family: "Tinos", serif;
    font-size: 15px;
    fill: var(--amber-text);
  }
</style>
</head>
<body>
<main class="label-sheet">

  <svg class="label label--dark" viewBox="0 0 500 640" aria-label="Ambre Ridge Châtaignier label, dark version">
    <defs>
      <linearGradient id="honey" x1="0" y1="0" x2="0" y2="1">
        <stop offset="0" stop-color="var(--honey-deep)"/>
        <stop offset="0.55" stop-color="var(--honey-light)"/>
        <stop offset="1" stop-color="var(--honey-deep)"/>
      </linearGradient>
    </defs>
    <rect class="honey-field" x="0" y="0" width="500" height="640" rx="40"/>

    <g class="neck-tag">
      <rect class="label-shape" x="200" y="0" width="100" height="140"/>
      <circle class="brand-dot" cx="250" cy="62" r="6"/>
      <text class="brand-name brand-name--tag" x="250" y="98" text-anchor="middle">Ambre</text>
      <text class="brand-name brand-name--tag" x="250" y="126" text-anchor="middle">Ridge</text>
    </g>

    <g class="brand-triangle">
      <polygon class="label-shape" points="250,170 80,350 420,350"/>
      <text class="brand-name" x="250" y="296" text-anchor="middle">Ambre</text>
      <text class="brand-name" x="250" y="334" text-anchor="middle">Ridge</text>
    </g>

    <g class="appellation-band">
      <path class="label-shape" d="M50 372 Q250 346 450 372 L450 430 Q250 408 50 430 Z"/>
      <text class="appellation" x="250" y="412" text-anchor="middle">Chataîgnier</text>
    </g>

    <g class="origin-panel">
      <path class="label-shape" d="M40 458 Q250 432 460 458 Q450 612 250 620 Q50 612 40 458 Z"/>
      <text class="origin-country" x="250" y="512" text-anchor="middle">FRANCE</text>
      <text class="origin-region" x="250" y="544" text-anchor="middle">Midi-Pyrénées</text>
      <text class="net-weight" x="250" y="582" text-anchor="middle">250g</text>
    </g>
  </svg>

  <svg class="label label--light" viewBox="0 0 500 640" aria-label="Ambre Ridge Châtaignier label, light version">
    <rect class="honey-field" x="0" y="0" width="500" height="640" rx="40"/>

    <g class="neck-tag">
      <rect class="label-shape" x="200" y="0" width="100" height="140"/>
      <circle class="brand-dot" cx="250" cy="62" r="6"/>
      <text class="brand-name brand-name--tag" x="250" y="98" text-anchor="middle">Ambre</text>
      <text class="brand-name brand-name--tag" x="250" y="126" text-anchor="middle">Ridge</text>
    </g>

    <g class="brand-triangle">
      <polygon class="label-shape" points="250,170 80,350 420,350"/>
      <text class="brand-name" x="250" y="296" text-anchor="middle">Ambre</text>
      <text class="brand-name" x="250" y="334" text-anchor="middle">Ridge</text>
    </g>

    <g class="appellation-band">
      <path class="label-shape" d="M50 372 Q250 346 450 372 L450 430 Q250 408 50 430 Z"/>
      <text class="appellation" x="250" y="412" text-anchor="middle">Chataîgnier</text>
    </g>

    <g class="origin-panel">
      <path class="label-shape" d="M40 458 Q250 432 460 458 Q450 612 250 620 Q50 612 40 458 Z"/>
      <text class="origin-country" x="250" y="512" text-anchor="middle">FRANCE</text>
      <text class="origin-region" x="250" y="544" text-anchor="middle">Midi-Pyrénées</text>
      <text class="net-weight" x="250" y="582" text-anchor="middle">250g</text>
    </g>
  </svg>

</main>
</body>
</html>
```